依頼詳細
印刷はカスタリオを予定しています。
専用のテンプレートの使用をお願いします。
https://www.castario.jp/download/temp_card.php
二つ折り名刺
110×91mm,55×182mm
記載項目
■入れたい要素
・「ハゲにくい猫首輪」
・「手作り、国産」
・「5000人以上の飼い主さんが愛用」
・お客様の声 https://www.mimitoro.jp/feature/
・サイズ表 https://www.mimitoro.jp/feature/column/2017081301
自分の愛猫ちゃんのサイズを書き込めるように
・ショップ名、URL
希望イメージ
シンプル 複雑
単色 カラフル
暗い 明るい
日常 高級
遊び心 厳粛
未来的 伝統的
女性的 男性的
希望する色
赤系
納品ファイル
• 高解像度JPG (.jpg)
• イラストレーター形式 (.ai)
補足説明
ロゴデータは添付ファイルをご使用ください
■ 選んだ理由

この度はご提案いただきまして、誠にありがとうございます。
当店のコンセプトや雰囲気をよくご理解いただき、素敵なデザインをご提案いただけました。

ありがとうございました。

■ 提案者全員のお礼・コメント

この度はたくさんのご提案いただきまして、誠にありがとうございました。

```html
<!DOCTYPE html>
<html lang="ja">
<head>
<meta charset="utf-8">
<title>みみとろ 二つ折りカード</title>
<link href="https://fonts.googleapis.com/css2?family=M+PLUS+Rounded+1c:wght@400;700;800&family=Noto+Sans+JP:wght@400;500&display=swap" rel="stylesheet">
<style>
  :root {
    --berry: #a5306a;
    --leaf: #8cc63f;
    --leaf-dark: #6fae2c;
    --leaf-soft: #b9db8c;
    --sky-soft: #a9d6e6;
    --rose: #e2688a;
    --ink: #333333;
    --paper: #ffffff;
    --line: #222222;
  }
  * { margin: 0; padding: 0; box-sizing: border-box; }
  html, body { width: 1200px; height: 3972px; overflow: hidden; background: var(--paper); }
  body { position: relative; font-family: "M PLUS Rounded 1c", sans-serif; color: var(--ink); }

  .side-label {
    position: absolute; left: 0; width: 1200px; text-align: center;
    font-family: "Noto Sans JP", sans-serif; font-size: 84px; font-weight: 400; color: #000;
  }
  .side-label--front { top: 100px; }
  .side-label--back { top: 2040px; }

  .front-cover {
    position: absolute; left: 112px; top: 312px; width: 976px; height: 1600px;
    background: var(--berry);
    display: flex; flex-direction: column; align-items: center; justify-content: center;
  }
  .brand { display: flex; align-items: center; gap: 22px; white-space: nowrap; }
  .brand__dot { width: 70px; height: 70px; border-radius: 50%; background: currentColor; }
  .brand__name { font-weight: 800; letter-spacing: 6px; }
  .front-cover .brand { color: var(--paper); margin-top: -120px; }
  .front-cover .brand__name { font-size: 104px; }
  .brand__tagline { color: var(--paper); font-size: 26px; font-weight: 700; letter-spacing: 3px; margin-top: 10px; margin-left: 90px; }

  .back-cover {
    position: absolute; left: 112px; top: 2192px; width: 976px; height: 1680px;
    border: 3px solid var(--line); background: var(--paper);
  }
  .banner { position: absolute; left: 64px; top: 68px; width: 840px; height: 124px; }
  .banner__text {
    position: absolute; left: 0; top: 0; width: 840px; height: 110px; display: flex; align-items: center; justify-content: center;
    color: var(--paper); font-weight: 800; font-size: 58px; letter-spacing: 3px; white-space: nowrap;
  }

  .worries { position: absolute; left: 40px; top: 210px; width: 896px; height: 300px; }
  .worries__cat { position: absolute; left: 20px; top: 60px; width: 210px; height: 220px; border-radius: 40px 40px 20px 20px;
    background: linear-gradient(180deg, #e9f4dc, #d3eab8); }
  .cloud { position: absolute; display: flex; align-items: center; justify-content: center; text-align: center;
    font-size: 25px; line-height: 1.35; color: var(--ink); white-space: nowrap; }
  .cloud svg { position: absolute; left: 0; top: 0; }
  .cloud span { position: relative; }

  .lead {
    position: absolute; left: 64px; top: 532px; font-size: 34px; color: var(--ink); white-space: nowrap;
    border-bottom: 3px solid var(--leaf); padding-bottom: 6px; padding-right: 20px;
  }
  .concept, .closing {
    position: absolute; left: 0; width: 976px; text-align: center; color: var(--rose);
    font-size: 40px; line-height: 1.45; font-weight: 500; white-space: nowrap;
  }
  .concept { top: 600px; }
  .closing { top: 1240px; }

  .feature { position: absolute; left: 64px; width: 860px; display: flex; align-items: center; gap: 28px; }
  .feature--handmade { top: 732px; }
  .feature--comfort { top: 900px; }
  .feature--safety { top: 1068px; }
  .feature__badge {
    flex: 0 0 132px; height: 132px; border-radius: 50%; background: var(--leaf);
    display: flex; align-items: center; justify-content: center; white-space: nowrap;
    color: var(--ink); font-size: 28px; font-weight: 700; letter-spacing: -1px;
  }
  .feature--handmade .feature__badge { background: var(--leaf-soft); }
  .feature--safety .feature__badge { background: var(--sky-soft); }
  .feature__text { font-size: 30px; line-height: 1.45; color: var(--ink); white-space: nowrap; }

  .back-cover .brand { position: absolute; left: 0; width: 976px; top: 1380px; justify-content: center; color: var(--berry); gap: 14px; }
  .back-cover .brand__dot { width: 44px; height: 44px; }
  .back-cover .brand__name { font-size: 66px; }
  .shop-type { position: absolute; left: 0; width: 976px; top: 1496px; text-align: center; font-size: 30px; color: var(--ink); }
  .shop-url { position: absolute; left: 0; width: 976px; top: 1548px; text-align: center; font-size: 40px; color: var(--ink);
    font-family: "Noto Sans JP", sans-serif; }
</style>
</head>
<body>
  <div class="side-label side-label--front">表紙</div>
  <section class="front-cover">
    <div class="brand">
      <span class="brand__dot"></span>
      <span class="brand__name">みみとろ</span>
    </div>
    <p class="brand__tagline">CAT COLLAR FACTORY MIMITORO</p>
  </section>

  <div class="side-label side-label--back">裏表紙</div>
  <section class="back-cover">
    <div class="banner">
      <svg width="840" height="124" viewBox="0 0 840 124">
        <polygon points="0,14 60,14 60,124 0,124 26,69" fill="var(--leaf-dark)"/>
        <polygon points="840,14 780,14 780,124 840,124 814,69" fill="var(--leaf-dark)"/>
        <rect x="40" y="0" width="760" height="110" fill="var(--leaf)"/>
      </svg>
      <div class="banner__text">みみとろ の猫首輪</div>
    </div>

    <div class="worries">
      <div class="worries__cat" role="img" aria-label="首輪をつけた猫の線画イラスト"></div>
      <div class="cloud" style="left:262px; top:20px; width:290px; height:140px;">
        <svg viewBox="0 0 290 140" width="290" height="140"><ellipse cx="145" cy="70" rx="139" ry="64" fill="none" stroke="var(--leaf)" stroke-width="5"/></svg>
        <span>首輪を嫌がって<br>しまうの・・・</span>
      </div>
      <div class="cloud" style="left:570px; top:20px; width:316px; height:140px;">
        <svg viewBox="0 0 316 140" width="316" height="140"><ellipse cx="158" cy="70" rx="152" ry="64" fill="none" stroke="var(--leaf)" stroke-width="5"/></svg>
        <span>首の被毛が<br>ハゲてしまう・・・</span>
      </div>
      <div class="cloud" style="left:390px; top:152px; width:310px; height:140px;">
        <svg viewBox="0 0 310 140" width="310" height="140"><ellipse cx="155" cy="70" rx="149" ry="64" fill="none" stroke="var(--leaf)" stroke-width="5"/></svg>
        <span>首輪が引っかかる<br>事故が心配・・・</span>
      </div>
    </div>

    <p class="lead">そんなお悩みをお持ちの飼い主さんへ</p>
    <p class="concept">『優しさ』がコンセプトの<br>みみとろの猫首輪ならきっと大丈夫です♪</p>

    <div class="feature feature--handmade">
      <div class="feature__badge">手作り</div>
      <p class="feature__text">国内で猫首輪職人がひとつひとつ丁寧に<br>仕上げます。大量生産品ではできない<br>細かいこだわりと高い品質が自慢です。</p>
    </div>
    <div class="feature feature--comfort">
      <div class="feature__badge">着け心地</div>
      <p class="feature__text">こだわりの柔らかい素材を厳選しています。<br>とてもソフトな着け心地と驚くほどの軽さで<br>猫ちゃんが嫌がらず、ハゲにくい首輪です。</p>
    </div>
    <div class="feature feature--safety">
      <div class="feature__badge">安全性</div>
      <p class="feature__text">全て安全仕様です。首輪が引っかかったり<br>しないよう、セーフティ・アジャスター<br>(flexlock社製)を採用しています。</p>
    </div>

    <p class="closing">あなたと愛猫ちゃんの<br>豊かで楽しい暮らしの一助となれば幸いです。</p>

    <div class="brand">
      <span class="brand__dot"></span>
      <span class="brand__name">みみとろ</span>
    </div>
    <p class="shop-type">猫首輪通販専門店</p>
    <p class="shop-url">https://www.mimitoro.jp/</p>
  </section>
</body>
</html>
```